Beautiful e-comm site for 'roadside farmers stand' online!

Need a logo design and basic e-comm website (super super simple) for new business called Brambletoft. Brambletoft is an online farmers stand where local artisans can sell 'brambletoft' goods directly from their makers!

Looking for something simple, whimsicle and clean! (Ideally with a light grey or perrywinkle and some color mixed in - word 'Brambletoft' in black - can work the pear shape in somewhere but not required!)

Target Market(s)

Hobby shoppers and 'quilo' goers who want a focus on edible things and care about ingredients!

Industry/Entity Type

E-Commerce

Number of Pages Required

2 page

Font styles to use
Decorative
Script

Colors
f3f1f8
ec1f27
cadf82

Requirements
Must have
• - Basic logo
• - Homepage
• - Product Detail Page
• - Be in a responsive, woocommerce or shopify, wordpress theme (will purchase theme after design is approved)
Nice to have
• - Matching check out & cart pages
• - 'About Us' page
• - SEO plugin
Should not have
• A cluttered look/feel.

```html
<!DOCTYPE html>
<html lang="en">
<head>
<meta charset="utf-8">
<title>Brambletoft — Online Farmers Stand</title>
<link href="https://fonts.googleapis.com/css2?family=Poppins:wght@400;500;600;700&family=Noto+Serif:wght@400&family=Hind:wght@700&display=swap" rel="stylesheet">
<style>
  :root {
    --white: #ffffff;
    --ink: #2b2b2b;
    --muted: #9a9aa6;
    --line: #dcdce4;
    --red: #ec1f27;
    --green: #5e8f1e;
    --blue: #1a7ff0;
    --yellow: #ffcc00;
    --mist: #f3f5f8;
    --periwinkle: #f3f1f8;
  }
  * { box-sizing: border-box; margin: 0; padding: 0; }
  html, body { width: 1200px; height: 1200px; overflow: hidden; background: var(--white); }
  body { position: relative; font-family: "Poppins", sans-serif; color: var(--ink); }

  .brand { position: absolute; left: 88px; top: 42px; font-family: "Poppins", sans-serif; font-weight: 600; font-size: 26px; color: var(--green); letter-spacing: -0.5px; }

  .search { position: absolute; left: 376px; top: 47px; width: 606px; height: 25px; border: 1px solid var(--line); border-radius: 13px; display: flex; align-items: center; }
  .search .refine { width: 144px; height: 100%; border-right: 1px solid var(--line); display: flex; align-items: center; justify-content: space-between; padding: 0 12px 0 12px; font-size: 9px; color: var(--red); }
  .search .query { flex: 1; padding-left: 16px; font-size: 9px; color: #b4b4be; }
  .search .go { width: 31px; height: 19px; border-radius: 10px; background: var(--blue); margin-right: 2px; display: flex; align-items: center; justify-content: center; }

  .round { position: absolute; top: 44px; width: 31px; height: 31px; border-radius: 50%; border: 1px solid var(--line); display: flex; align-items: center; justify-content: center; background: var(--white); }
  .cart { left: 1000px; }
  .cart .count { position: absolute; top: -7px; right: -2px; background: var(--blue); color: var(--white); font-size: 8px; font-weight: 600; border-radius: 6px; padding: 0 4px; line-height: 11px; }
  .avatar { left: 1046px; top: 45px; width: 29px; height: 29px; border: none; background: radial-gradient(circle at 50% 45%, #c99a82 0 35%, #2a1d1a 38%); }
  .menu { left: 1085px; }

  .tags { position: absolute; left: 388px; width: 560px; }
  .tags h2 { font-size: 13px; font-weight: 400; margin-bottom: 8px; color: #222; }
  .tag-row { display: flex; gap: 6.5px; margin-bottom: 13px; }
  .tag { width: 56px; height: 12px; border: 1px solid #c8c8d0; border-radius: 6px; font-size: 7px; text-align: center; line-height: 10px; color: #444; box-shadow: 0 1px 2px rgba(0,0,0,0.08); }
  .tag.active { background: var(--red); border-color: var(--red); color: var(--white); font-weight: 600; }
  .tags.foods { top: 90px; }
  .tags.products { top: 165px; }

  .hero-visual { position: absolute; left: 0; top: 274px; }

  .hero-copy { position: absolute; left: 89px; top: 362px; }
  .countdown { font-size: 12px; color: var(--green); }
  .hero-copy h1 { font-family: "Noto Serif", serif; font-weight: 400; font-size: 47px; line-height: 46px; margin-top: 8px; color: #2a2a2a; letter-spacing: 0.3px; }
  .offer { margin-top: 18px; font-size: 8px; line-height: 13px; color: #a4a4b0; }
  .offer em { font-style: normal; color: var(--red); }
  .shop-now { display: inline-block; margin-top: 16px; width: 88px; height: 25px; border-radius: 13px; background: var(--yellow); color: var(--white); font-size: 7.5px; font-weight: 700; text-align: center; line-height: 25px; box-shadow: 0 6px 10px rgba(255, 204, 0, 0.35); }

  .share { position: absolute; left: 95px; top: 657px; }
  .share p { font-size: 9px; color: #b2b2bc; }
  .share ul { list-style: none; display: flex; gap: 17px; margin-top: 20px; }
  .share li { width: 9px; height: 9px; border-radius: 2px; background: #c4c4cc; }

  .category { position: absolute; top: 822px; width: 600px; height: 378px; display: flex; align-items: center; justify-content: center; padding-bottom: 4px; }
  .category span { font-family: "Hind", sans-serif; font-weight: 700; font-size: 42px; color: var(--white); letter-spacing: 0.5px; margin-top: -8px; }
  .category.foods { left: 0; background: linear-gradient(160deg, #c86ad0 0%, #e0609c 45%, #f06f7a 75%, #b06aa8 100%); }
  .category.products { left: 600px; background: linear-gradient(200deg, #4a2a5e 0%, #7a2a86 40%, #a83a9a 65%, #5a2a72 100%); }
</style>
</head>
<body>
  <div class="brand">Brambletoft</div>

  <div class="search">
    <div class="refine">Refine your search
      <svg width="10" height="12" viewBox="0 0 10 12"><path d="M1 1h8L6 5v6L4 10V5z" fill="none" stroke="#ec1f27" stroke-width="1"/></svg>
    </div>
    <div class="query">What are you looking for?</div>
    <div class="go"><svg width="10" height="10" viewBox="0 0 10 10"><circle cx="4.2" cy="4.2" r="3" fill="none" stroke="#fff" stroke-width="1.4"/><path d="M6.5 6.5L9 9" stroke="#fff" stroke-width="1.4"/></svg></div>
  </div>

  <div class="round cart">
    <svg width="12" height="11" viewBox="0 0 12 11"><path d="M0.5 1h2l1.5 6h6l1.3-4.5H3" fill="none" stroke="#444" stroke-width="1"/><circle cx="4.5" cy="9.5" r="0.9" fill="#444"/><circle cx="9" cy="9.5" r="0.9" fill="#444"/></svg>
    <span class="count">18</span>
  </div>
  <div class="round avatar" role="img" aria-label="Shopper profile photo"></div>
  <div class="round menu">
    <svg width="10" height="8" viewBox="0 0 10 8"><path d="M1 1.5h8M1 4h8M1 6.5h8" stroke="#444" stroke-width="1"/></svg>
  </div>

  <section class="tags foods">
    <h2>#homemadefoods</h2>
    <div class="tag-row"><span class="tag active">cookies</span><span class="tag">cake</span><span class="tag">jellies</span><span class="tag">jams</span><span class="tag">pickles</span><span class="tag">cookies</span><span class="tag">jellies</span><span class="tag">jams</span><span class="tag">pickles</span></div>
    <div class="tag-row"><span class="tag">jellies</span><span class="tag">cookies</span><span class="tag">cookies</span><span class="tag">jellies</span><span class="tag">jams</span><span class="tag">pickles</span><span class="tag">cookies</span></div>
  </section>
  <section class="tags products">
    <h2>#homeproducts</h2>
    <div class="tag-row"><span class="tag">jams</span><span class="tag">cake</span><span class="tag">jellies</span><span class="tag active">cookies</span><span class="tag">pickles</span><span class="tag">cookies</span><span class="tag">jellies</span><span class="tag">jams</span><span class="tag">pickles</span></div>
    <div class="tag-row"><span class="tag">jellies</span><span class="tag">cookies</span><span class="tag">cookies</span><span class="tag">jellies</span><span class="tag">jams</span><span class="tag">pickles</span><span class="tag">cookies</span></div>
  </section>

  <svg class="hero-visual" width="1200" height="548" viewBox="0 274 1200 548">
    <defs>
      <linearGradient id="jarTone" x1="0" y1="0" x2="1" y2="1">
        <stop offset="0" stop-color="#f3c418"/>
        <stop offset="0.5" stop-color="#f0b81c"/>
        <stop offset="1" stop-color="#e6b21a"/>
      </linearGradient>
    </defs>
    <path d="M581,274 A440 440 0 0 0 623,822 L1200,822 L1200,274 Z" fill="var(--mist)"/>
    <path role="img" aria-label="Rows of homemade preserve jars with gingham lids" d="M605,274 A440 440 0 0 0 647,822 L1200,822 L1200,274 Z" fill="url(#jarTone)"/>
  </svg>

  <div class="hero-copy">
    <p class="countdown">02 days left</p>
    <h1>Winter is<br>almost over</h1>
    <p class="offer">Update your wishlist and get <em>25% discount</em><br>on selected items only</p>
    <a class="shop-now">SHOP NOW</a>
  </div>

  <div class="share">
    <p>Share with friends</p>
    <ul><li></li><li></li><li></li><li></li><li></li></ul>
  </div>

  <div class="category foods" role="img" aria-label="Layered cake on a plate beside a small tower ornament and potted plant"><span>HOMEMADE FOODS</span></div>
  <div class="category products" role="img" aria-label="Open glass jar of pickles with dill and cucumber slices"><span>HOME PRODUCTS</span></div>
</body>
</html>
```